Letterhead and Envelopes design using existing logo. Logo can be found at tqvanholt.com

Use existing logo (attached) and incorporate in letterhead and envelope designs.

Current logo can be viewed at tqvanholt.com the web site reflect various parent and sub companies. Please see attached as well.

Target Market(s)

Other oil and gas operators.

Industry/Entity Type

Oil And Gas

Font styles to use
Sans Serif

Colors

Designer to choose colors to be used in the design.

Requirements
Must have
• Current logo and address
Nice to have
• Modern, contemporary approach yet incorporate existing traditional design.
• After design is selected for Wexford Tiller Holdings I will use similar design for Royalties, Exploration, Energy and Farms with different color schemes.

```html
<!DOCTYPE html>
<html lang="en">
<head>
<meta charset="utf-8">
<title>Wexford Tiller Holdings — Stationery</title>
<link rel="stylesheet" href="https://fonts.googleapis.com/css2?family=Questrial&family=Roboto:wght@400&display=swap">
<style>
  :root {
    --stage: #dcdcdc;
    --paper: #f1f1f1;
    --brand-green: #6e993a;
    --ink-black: #000000;
    --text-grey: #555555;
    --text-dark: #3f3f3f;
    --white: #ffffff;
    --signature-blue: #2d5fb0;
  }
  * { margin: 0; padding: 0; box-sizing: border-box; }
  html, body { width: 1200px; height: 877px; overflow: hidden; }
  body {
    background: var(--stage);
    position: relative;
    font-family: "Questrial", sans-serif;
  }
  .sheet { position: absolute; background: var(--paper); overflow: hidden; }

  /* Letterhead */
  .letterhead { left: 69px; top: 64px; width: 527px; height: 742px; }
  .brand-band {
    position: absolute; left: 0; height: 77px; width: 100%;
    background: var(--brand-green);
  }
  .letterhead .brand-band { top: 32px; }
  .brand-block {
    position: absolute; left: 0; top: 0; height: 100%;
    background: var(--ink-black);
  }
  .letterhead .brand-block { width: 80px; }
  .brand-mark {
    position: absolute; border-radius: 50%; background: var(--white);
  }
  .letterhead .brand-mark { left: 34px; top: -3px; width: 82px; height: 82px; }
  .brand-name {
    position: absolute; color: var(--white);
    font-family: "Questrial", sans-serif; font-size: 15px; white-space: nowrap;
  }
  .letterhead .brand-name { left: 130px; top: 30px; }
  .contact {
    position: absolute; left: 376px; top: 16px;
    font-family: "Roboto", sans-serif; font-size: 8px; line-height: 10px;
    color: var(--white);
  }
  .contact .address { margin-bottom: 5px; }
  .contact .line { display: flex; align-items: center; gap: 4px; }
  .contact svg { width: 7px; height: 7px; fill: var(--white); }

  .letter-body {
    position: absolute; left: 45px; top: 211px; width: 439px;
    color: var(--text-grey);
  }
  .salutation { font-size: 14px; color: var(--text-dark); margin-bottom: 21px; }
  .letter-body p {
    font-size: 7.6px; line-height: 11.4px; margin-bottom: 11.4px;
    text-align: justify;
  }
  .closing { font-size: 7.6px; margin-top: 20px; }
  .signature {
    position: absolute; left: 41px; top: 520px; width: 94px; height: 38px;
    background: linear-gradient(90deg, rgba(45,95,176,0.25), rgba(45,95,176,0.12));
    border-radius: 4px;
  }

  /* Envelope back */
  .envelope-back { left: 614px; top: 268px; width: 531px; height: 241px; }
  .flap { position: absolute; left: 0; top: 0; width: 531px; height: 88px; }
  .flap-brand {
    position: absolute; left: 0; top: 33px; width: 531px;
    display: flex; justify-content: center; align-items: center; gap: 6px;
  }
  .flap-brand .dot {
    width: 14px; height: 14px; border-radius: 50%; background: var(--ink-black);
  }
  .flap-brand .name { font-size: 12px; color: var(--ink-black); }

  /* Envelope front */
  .envelope-front { left: 614px; top: 562px; width: 532px; height: 241px; }
  .envelope-front .brand-band { top: 21px; }
  .envelope-front .brand-block { width: 26px; }
  .envelope-front .brand-mark { left: 24px; top: -3px; width: 82px; height: 82px; }
  .envelope-front .address-block {
    position: absolute; left: 129px; top: 34px;
    font-family: "Roboto", sans-serif; font-size: 8px; line-height: 10px;
    color: var(--white);
  }
  .envelope-front .brand-name { left: 129px; top: 14px; font-size: 12px; }
</style>
</head>
<body>

  <section class="sheet letterhead">
    <header class="brand-band">
      <div class="brand-block"></div>
      <div class="brand-mark"></div>
      <span class="brand-name">Wexford Tiller Holdings</span>
      <div class="contact">
        <div class="address">PO Box 418 Larkfield<br>North Dakota 58990</div>
        <div class="line">
          <svg viewBox="0 0 10 10"><path d="M2 0.5 L3.6 0.5 L4.3 2.8 L3.2 3.8 Q4.2 5.9 6.2 6.8 L7.2 5.7 L9.5 6.4 L9.5 8 Q9.5 9.5 8 9.5 Q1 9 0.5 2 Q0.5 0.5 2 0.5 Z"/></svg>
          <span>(555) 014.2290</span>
        </div>
        <div class="line">
          <svg viewBox="0 0 10 10"><path d="M0 1.5 H10 V8.5 H0 Z M0.6 2 L5 5.4 L9.4 2 Z" fill-rule="evenodd"/></svg>
          <span>reception@tqvanholt.com</span>
        </div>
        <div class="line">
          <svg viewBox="0 0 10 10"><circle cx="5" cy="5" r="4.6"/></svg>
          <span>www.tqvanholt.com</span>
        </div>
      </div>
    </header>

    <article class="letter-body">
      <div class="salutation">Dear Mr. Harlan,</div>
      <p>Lorem ipsum dolor sit amet, consectetur adipiscing elit. Donec orci purus, luctus vitae dignissim eu, iaculis sed purus. Vivamus faucibus, ipsum nec aliquet viverra, leo mauris condimentum ligula, sit amet sagittis enim ligula quis arcu. Nam egestas tortor id nisi porttitor mattis. In tortor ante, ultricies in suscipit a, tempus non massa. Vivamus et auctor mi. Fusce vel massa nulla. Phasellus nec eros mauris, et scelerisque orci.</p>
      <p>Donec malesuada orci vitae nulla accumsan porta a id massa. Quisque accumsan iaculis magna sit amet fringilla. Maecenas consequat, magna eget tincidunt semper, odio nibh rutrum mi, id feugiat ante nisi eu risus. Vestibulum nunc orci, rhoncus a placerat in, ultricies in mi. Cras mattis varius eros, vel fringilla nisi suscipit eget. Quisque scelerisque sagittis nulla at porttitor.</p>
      <p>Sed id augue vitae urna euismod commodo aliquet a quam. Pellentesque arcu velit, cursus et malesuada ut, consequat et diam. Nullam erat sem, rhoncus id ullamcorper vitae, rhoncus et arcu. In ultricies ultricies nulla, ut rutrum nisi iaculis at. Donec eu magna a metus ornare faucibus. Fusce aliquet faucibus ultricies. Morbi semper, est id tincidunt gravida, sem arcu adipiscing lacus, ac bibendum nulla leo eu purus. Quisque nec diam sed risus consectetur a ccumsan quis quis nibh. Vestibulum id purus lorem.</p>
      <p>It is a long established fact that a reader will be distracted by the readable content of a page when looking at its layout. The point of using Lorem Ipsum is that it has a more-or-less normal distribution of letters, as opposed to using 'Content here, content here', making it look like readable English. Many desktop publishing packages</p>
      <div class="closing">Sincerely,</div>
    </article>
    <div class="signature" role="img" aria-label="Handwritten signature of the sender"></div>
  </section>

  <section class="sheet envelope-back">
    <svg class="flap" viewBox="0 0 531 88" aria-hidden="true">
      <path d="M0 0 H531 L522 55 Q516 88 488 88 H43 Q15 88 9 55 Z" fill="var(--brand-green)"/>
    </svg>
    <div class="flap-brand">
      <span class="dot"></span>
      <span class="name">Wexford Tiller Holdings</span>
    </div>
  </section>

  <section class="sheet envelope-front">
    <header class="brand-band">
      <div class="brand-block"></div>
      <div class="brand-mark"></div>
      <span class="brand-name">Wexford Tiller Holdings</span>
      <div class="address-block">PO Box 418 Larkfield<br>North Dakota 58990</div>
    </header>
  </section>

</body>
</html>
```